Veltrop Partners Website - developing a website for a new IIoT (Industrial Internet of Things) startup

Hi All-

Thought I'd re-write this bit...

Firstly, to everyone who has submitted designs, thank you.

Basically, we are looking for a simple/ elegant / modern website with clean lines and design. Because this is a startup, we don't have a great deal of content. Therefore, I'm relying on the site to give us an established / international feel (no images of London, London attractions, or the London skyline please!) We will have offices in London / LA and Tokyo by the end of this year.

Selecting great images is really important. As I say, abstract is fine (less literal.) Black and white is fine as well. We need to convey our expertise to new, international clients, so this is v.important.

http://www.brevanti41.it/ (favourite)
http://www.crafthollowstudio.com/cases/

In terms of colour, I think white /grey/ black and maybe experiment with red for the word Veltrop and (possibly) Group. Please note** I need the following words / strap line written underneath the main logo: IIoT Strategy. Sensor Innovation. Machine Learning.

Whomever we chose to work with, this will be an ongoing partnership: we will continually need to add new content and update the site.

Thank you!

Dell.
Updates

**Please view updated brief description.

Target Market(s)

Mid-sized (£25M- £500M GBP) companies in the UK/ US and Asia. Facilities/ Construction/ Automotive/ Manufacturing / Engineering

Industry/Entity Type

Information Technology

Logo Text

Veltrop Partners -- IIoT Strategy. Sensor Innovation. Machine Learning (written underneath)

Coding

Coded - Design and coding required

Number of Pages Required

5+ page

Font styles to use
Sans Serif

Requirements
Must have
• An international, established, aspirational feel. Beautiful imagery. elegant infographics (nothing complex). CTA on homepage.
Should not have
• Anything cartoony / informal or naff corporate imagery.

```html
<!DOCTYPE html>
<html lang="en">
<head>
<meta charset="utf-8">
<title>Veltrop Partners</title>
<link href="https://fonts.googleapis.com/css2?family=Open+Sans:wght@400;600;700&display=swap" rel="stylesheet">
<style>
:root{
  --red:#c0272d;
  --ink:#333333;
  --text:#555555;
  --muted:#888888;
  --line:#d8d8d8;
  --paper:#ffffff;
  --mist:#f3f3f3;
  --card:#f1f1f1;
  --field:#f7f7f7;
  --footer:#333333;
  --footer-text:#9a9a9a;
}
*{box-sizing:border-box;margin:0;padding:0}
html,body{width:1200px;height:2922px;overflow:hidden}
body{font-family:"Open Sans",Arial,sans-serif;color:var(--text);background:var(--paper);position:relative}

/* header */
.site-header{position:absolute;top:0;left:0;width:1200px;height:93px;background:var(--paper);z-index:2}
.brand{position:absolute;left:130px;top:16px;font-size:30px;font-weight:700;letter-spacing:0.5px;color:var(--red);line-height:40px;white-space:nowrap}
.strapline{position:absolute;left:131px;top:58px;font-size:11px;letter-spacing:0.3px;color:var(--muted);line-height:14px;white-space:nowrap}
.main-nav{position:absolute;right:132px;top:36px;display:flex;gap:28px;font-size:13px;color:var(--ink)}
.main-nav a{color:inherit;text-decoration:none}
.main-nav .active{color:var(--red);border-bottom:1px solid var(--red);padding-bottom:3px}

/* hero */
.hero{position:absolute;top:93px;left:0;width:1200px;height:521px;
  background:linear-gradient(180deg,#8fb4d8 0%,#c9dced 40%,#9aa6ad 70%,#6a7468 100%)}
.hero-arrow{position:absolute;top:240px;width:44px;height:44px;border-radius:50%;border:2px solid rgba(255,255,255,.8);background:rgba(0,0,0,.15)}
.hero-arrow svg{display:block;margin:12px auto}
.hero-arrow.prev{left:24px}.hero-arrow.next{right:24px}

/* section titles */
.section-title{position:absolute;left:0;width:1200px;text-align:center;font-size:26px;font-weight:400;color:var(--red)}
.section-title .rule{display:block;width:160px;height:1px;background:var(--line);margin:12px auto 0;position:relative}
.section-title .rule::after{content:"";position:absolute;left:40px;top:-1px;width:80px;height:3px;background:var(--red)}
.title-arrows{display:inline-flex;align-items:center;gap:22px}
.pager{width:24px;height:24px;border:1px solid #bbb;display:inline-flex;align-items:center;justify-content:center;background:var(--paper)}

/* quick contact */
.grey-band{position:absolute;left:0;top:614px;width:1200px;height:664px;background:var(--mist)}
.quick-contact{position:absolute;left:132px;top:537px;width:936px;height:303px;background:var(--paper)}
.field{position:absolute;height:42px;border:1px solid #dcdcdc;background:var(--field);font-size:11px;color:var(--muted);padding:13px 22px}
.submit{position:absolute;left:427px;top:215px;width:82px;height:40px;background:var(--ink);color:#fff;font-size:12px;font-weight:700;text-align:center;line-height:40px}

/* services */
.service{position:absolute;top:968px;width:290px;text-align:center}
.service .icon{height:85px;display:flex;align-items:flex-end;justify-content:center}
.service h3{margin-top:16px;font-size:21px;font-weight:700;color:var(--red)}
.service p{margin-top:6px;font-size:11px;line-height:16px;color:var(--text)}
.btn-ghost{display:inline-block;margin-top:14px;width:82px;height:30px;border:1px solid #ccc;background:var(--paper);font-size:11px;color:var(--muted);line-height:28px}

/* welcome */
.welcome-media{position:absolute;left:132px;top:1358px;width:456px;height:272px;background:linear-gradient(135deg,#2f2f2f,#1b1b1b)}
.welcome-copy{position:absolute;left:612px;top:1345px;width:456px;font-size:13px;line-height:21.5px;color:var(--ink)}
.welcome-copy h2{font-size:25px;font-weight:400;color:var(--red);width:186px;text-align:center;line-height:34px}
.welcome-copy .rule{display:block;width:186px;height:1px;background:var(--line);margin:8px 0 20px;position:relative}
.welcome-copy .rule::after{content:"";position:absolute;left:29px;top:-1px;width:104px;height:3px;background:var(--red)}
.welcome-copy p{margin-bottom:21px}
.divider{position:absolute;left:0;top:1710px;width:1200px;height:1px;background:#e2e2e2}

/* events */
.event-card{position:absolute;top:1846px;width:287px;height:134px;background:var(--card);padding:20px 22px}
.event-card .date{font-size:12px;color:var(--red)}
.event-card p{margin-top:10px;font-size:14px;line-height:20px;color:var(--ink)}

/* blog */
.blog-band{position:absolute;left:0;top:2058px;width:1200px;height:537px;background:var(--mist)}
.post{position:absolute;top:2202px;width:298px}
.post .thumb{height:160px}
.post h4{margin-top:14px;font-size:14px;font-weight:400;line-height:20px;color:var(--ink)}
.post .date{margin-top:8px;font-size:11px;color:var(--ink)}
.post p{margin-top:6px;font-size:10px;line-height:15px;color:var(--muted)}
.post .more{margin-top:6px;font-size:10px;font-weight:600;color:var(--ink)}

/* cta */
.cta-line{position:absolute;left:0;top:2670px;width:1200px;text-align:center;font-size:16px;color:var(--ink)}
.cta-btn{position:absolute;left:536px;top:2701px;width:128px;height:44px;background:var(--red);color:#fff;font-size:14px;font-weight:700;text-align:center;line-height:44px}

/* footer */
.site-footer{position:absolute;left:0;top:2822px;width:1200px;height:100px;background:var(--footer)}
.footer-nav{position:absolute;left:132px;top:20px;font-size:11px;color:var(--footer-text)}
.footer-nav span{margin:0 6px}
.copyright{position:absolute;left:132px;top:44px;font-size:11px;color:var(--footer-text)}
.social{position:absolute;right:148px;top:28px;display:flex;gap:14px}
.social span{width:26px;height:26px;border-radius:50%;border:1px solid #777}
</style>
</head>
<body>

<header class="site-header">
  <div class="brand">VELTROP PARTNERS</div>
  <div class="strapline">IIoT Strategy. Sensor Innovation. Machine Learning.</div>
  <nav class="main-nav">
    <a class="active">Home</a><a>About</a><a>Strategy</a><a>Sensors</a><a>Data &amp; AI</a><a>Events</a><a>Blog</a><a>Contact</a>
  </nav>
</header>

<section class="hero" role="img" aria-label="Wide photograph of a city skyline with bridge and towers under a blue sky">
  <div class="hero-arrow prev"><svg width="16" height="16" viewBox="0 0 16 16"><path d="M11 2 5 8l6 6" fill="none" stroke="#fff" stroke-width="2"/></svg></div>
  <div class="hero-arrow next"><svg width="16" height="16" viewBox="0 0 16 16"><path d="M5 2l6 6-6 6" fill="none" stroke="#fff" stroke-width="2"/></svg></div>
</section>

<div class="grey-band"></div>

<section class="quick-contact">
  <h2 class="section-title" style="top:40px;width:936px">Quick Contact<span class="rule"></span></h2>
  <div class="field" style="left:12px;top:108px;width:218px">Name</div>
  <div class="field" style="left:244px;top:108px;width:218px">Email</div>
  <div class="field" style="left:476px;top:108px;width:218px">Phone</div>
  <div class="field" style="left:708px;top:108px;width:218px">Company</div>
  <div class="field" style="left:12px;top:163px;width:914px">Message</div>
  <div class="submit">SUBMIT</div>
</section>

<h2 class="section-title" style="top:895px">Our Services<span class="rule"></span></h2>

<div class="service" style="left:130px">
  <div class="icon"><svg width="44" height="80" viewBox="0 0 44 80" fill="#333"><rect x="19" y="0" width="6" height="16"/><rect x="14" y="5" width="16" height="6"/><path d="M10 20h24l-4 10H14z"/><path d="M15 32h14l3 32H12z"/><rect x="6" y="66" width="32" height="6"/><rect x="2" y="73" width="40" height="7"/></svg></div>
  <h3>STRATEGY</h3>
  <p>Donec porttitor turpis sit amet arcu fringilla, ut tristique erat porta. Integer tellus non magna efficitur rutrum quis vel tortor interdum hendrerit.</p>
  <span class="btn-ghost">Read more</span>
</div>
<div class="service" style="left:455px">
  <div class="icon"><svg width="96" height="80" viewBox="0 0 96 80" fill="none" stroke="#333" stroke-width="8" stroke-linecap="round"><path d="M6 28a60 60 0 0 1 84 0"/><path d="M20 43a40 40 0 0 1 56 0"/><path d="M34 58a20 20 0 0 1 28 0"/><circle cx="48" cy="72" r="4" fill="#333"/></svg></div>
  <h3>SENSORS</h3>
  <p>Donec porttitor turpis sit amet arcu fringilla, ut tristique erat porta. Integer tellus non magna efficitur rutrum quis vel tortor interdum hendrerit.</p>
  <span class="btn-ghost">Read more</span>
</div>
<div class="service" style="left:780px">
  <div class="icon"><svg width="90" height="80" viewBox="0 0 90 80"><rect x="12" y="0" width="66" height="5" fill="#333"/><rect x="6" y="8" width="78" height="5" fill="#333"/><rect x="2" y="16" width="86" height="64" fill="#333"/><rect x="8" y="22" width="74" height="52" fill="#fff"/><rect x="12" y="26" width="66" height="44" fill="#333"/><path d="M36 34h12l8 8v18H36z" fill="#fff"/></svg></div>
  <h3>DATA &amp; AI</h3>
  <p>Donec porttitor turpis sit amet arcu fringilla, ut tristique erat porta. Integer tellus non magna efficitur rutrum quis vel tortor interdum hendrerit.</p>
  <span class="btn-ghost">Read more</span>
</div>

<div class="welcome-media" role="img" aria-label="Photograph of a thoughtful businessman beside chalkboard sketches of ideas and arrows"></div>
<div class="welcome-copy">
  <h2>Welcome</h2>
  <span class="rule"></span>
  <p>The core team at Veltrop Partners are Innovators, Engineers, PhDs and Data Scientists who assist mid-sized companies ($25M- $500M) to capitalise on the enormous potential of the Industrial Internet of Things (“IIoT.”)</p>
  <p>Our three business units –Strategy, Sensors and AI – mean that we can provide expert advice to both new entrants and companies already familiar with IIoT.</p>
  <p>Founded by our Chief Strategy Officer and serial entrepreneur, Dell Harwick, Veltrop is based in London and have plans to open offices in Tokyo and LA in</p>
</div>
<div class="divider"></div>

<h2 class="section-title" style="top:1780px"><span class="title-arrows"><span class="pager"><svg width="8" height="10"><path d="M6 1 2 5l4 4" fill="none" stroke="#999" stroke-width="1.5"/></svg></span>Events<span class="pager"><svg width="8" height="10"><path d="M2 1l4 4-4 4" fill="none" stroke="#999" stroke-width="1.5"/></svg></span></span><span class="rule"></span></h2>

<div class="event-card" style="left:132px"><div class="date">24 Feb, 2017</div><p>Morbi dictum bibendum magna, blandit egestas risus fringilla non. In commodo tempus posuere.</p></div>
<div class="event-card" style="left:457px"><div class="date">24 Feb, 2017</div><p>Morbi dictum bibendum magna, blandit egestas risus fringilla non. In commodo tempus posuere.</p></div>
<div class="event-card" style="left:781px"><div class="date">24 Feb, 2017</div><p>Morbi dictum bibendum magna, blandit egestas risus fringilla non. In commodo tempus posuere.</p></div>

<div class="blog-band"></div>
<h2 class="section-title" style="top:2130px"><span class="title-arrows"><span class="pager"><svg width="8" height="10"><path d="M6 1 2 5l4 4" fill="none" stroke="#999" stroke-width="1.5"/></svg></span>Blog<span class="pager"><svg width="8" height="10"><path d="M2 1l4 4-4 4" fill="none" stroke="#999" stroke-width="1.5"/></svg></span></span><span class="rule"></span></h2>

<article class="post" style="left:132px">
  <div class="thumb" role="img" aria-label="Photograph of a businessman in a red cape leaping over a floor" style="background:linear-gradient(135deg,#e6d6bf,#c8b293)"></div>
  <h4>Pellentesque pulvinar posuere velit et. Cura bitur sollicitudin efficitur egestas</h4>
  <div class="date">24 Feb, 2017</div>
  <p>Donec eget rhoncus nulla. Suspendisse tincidunt commodo cursus. Duis finibus tortor sapien, vel commodo augue tempor eu...</p>
  <div class="more">More</div>
</article>
<article class="post" style="left:451px">
  <div class="thumb" role="img" aria-label="Photograph of colleagues talking over coffee in an office" style="background:linear-gradient(135deg,#4a4d50,#8b7a5c)"></div>
  <h4>Pellentesque pulvinar posuere velit et. Cura bitur sollicitudin efficitur egestas</h4>
  <div class="date">24 Feb, 2017</div>
  <p>Donec eget rhoncus nulla. Suspendisse tincidunt commodo cursus. Duis finibus tortor sapien, vel commodo augue tempor eu...</p>
  <div class="more">More</div>
</article>
<article class="post" style="left:770px">
  <div class="thumb" role="img" aria-label="Photograph of people working at laptops in a bright office" style="background:linear-gradient(135deg,#d9dde0,#7d858c)"></div>
  <h4>Pellentesque pulvinar posuere velit et. Cura bitur sollicitudin efficitur egestas</h4>
  <div class="date">24 Feb, 2017</div>
  <p>Donec eget rhoncus nulla. Suspendisse tincidunt commodo cursus. Duis finibus tortor sapien, vel commodo augue tempor eu...</p>
  <div class="more">More</div>
</article>

<p class="cta-line">Morbi venenatis mauris dui, at laoreet orci sodales et. Phasellus leo velit, sagittis aliquet mollis in, placerat eu ante.</p>
<div class="cta-btn">CONTACT US</div>

<footer class="site-footer">
  <div class="footer-nav">Home<span>|</span>About<span>|</span>Strategy<span>|</span>Sensors<span>|</span>Data &amp; AI<span>|</span>Events<span>|</span>Blog<span>|</span>Contact</div>
  <div class="copyright">Copyright © 2017 Company name. All rights reserved.</div>
  <div class="social"><span></span><span></span><span></span><span></span><span></span></div>
</footer>

</body>
</html>
```